Travel Blogger Business Card for roamquill.net

I need a two-sided business card for a travel blogging website. The card should be both professional and fun at the same time. This is for the website www.roamquill.net

I don't necessarily think that the current logo on the website needs to be used on the business card but it can be. I am very flexible with ideas

Target Market(s)

Travel agencies that will be met at a conference.

Industry/Entity Type

Travel

Contact Information for Business Card

Company Name: Roam Quill.net
Name: Bertrand Olesky
Voice: +1-(345)-402-7731
Address: Coral Reach Shore, Grand Cayman, Cayman Islands
Email: ceo@roamquill.net

Colors
0592cd
0355a3
3176b5
33a6d7
85cae6
85acd3

Requirements
Must have
• Website address and name should be bigger than address, phone number, and email.

```html
<!DOCTYPE html>
<html lang="en">
<head>
<meta charset="utf-8">
<title>Roam Quill.net – Business Card</title>
<link rel="stylesheet" href="https://fonts.googleapis.com/css2?family=Arimo:wght@400&display=swap">
<style>
  :root {
    --page-bg: #e9eaec;
    --card-bg: #ffffff;
    --ink: #111111;
    --band-blue: #33a6d7;
    --band-ink: #ffffff;
    --card-edge: rgba(0, 0, 0, 0.08);
  }
  * { margin: 0; padding: 0; box-sizing: border-box; }
  html, body {
    width: 1200px;
    height: 1135px;
    overflow: hidden;
    background: var(--page-bg);
    font-family: "Arimo", Arial, sans-serif;
    color: var(--ink);
  }
  .canvas {
    position: relative;
    width: 1200px;
    height: 1135px;
  }
  .card {
    position: absolute;
    left: 237px;
    width: 679px;
    height: 407px;
    background: var(--card-bg);
    box-shadow: 0 0 0 1px var(--card-edge);
  }
  .card--front { top: 90px; }
  .card--back { top: 625px; }

  .holder-name {
    position: absolute;
    right: 28px;
    top: 60px;
    font-size: 27px;
    font-weight: 400;
    letter-spacing: 0.3px;
  }
  .contact-list {
    position: absolute;
    left: 28px;
    top: 304px;
    list-style: none;
    font-size: 14px;
    line-height: 18.5px;
  }
  .contact-item {
    display: flex;
    align-items: center;
  }
  .contact-icon {
    width: 11px;
    height: 11px;
    margin-right: 8px;
    fill: var(--ink);
    flex: none;
  }

  .web-band {
    position: absolute;
    left: 0;
    top: 161px;
    width: 100%;
    height: 85px;
    background: var(--band-blue);
    display: flex;
    align-items: center;
    justify-content: center;
    color: var(--band-ink);
    font-size: 22px;
    letter-spacing: 0.3px;
  }
  .web-icon {
    width: 19px;
    height: 19px;
    margin-right: 14px;
    margin-left: -12px;
  }
</style>
</head>
<body>
<main class="canvas">
  <section class="card card--front" aria-label="Card front">
    <h1 class="holder-name">Bertrand Olesky</h1>
    <ul class="contact-list">
      <li class="contact-item">
        <svg class="contact-icon" viewBox="0 0 12 12" aria-hidden="true">
          <path d="M3 1 L5 3.5 L4 4.8 Q5 7.2 7.2 8 L8.5 7 L11 9 L9.8 11 Q5.5 11 2.5 7.5 Q0.8 4.5 1.5 2 Z"/>
        </svg>
        <span>+1-(345)-402-7731</span>
      </li>
      <li class="contact-item">
        <svg class="contact-icon" viewBox="0 0 12 12" aria-hidden="true">
          <rect x="0.5" y="3" width="11" height="7"/>
        </svg>
        <span>ceo@roamquill.net</span>
      </li>
      <li class="contact-item">
        <svg class="contact-icon" viewBox="0 0 12 12" aria-hidden="true">
          <path d="M6 0.5 A4 4 0 0 1 10 4.5 C10 7.5 6 11.5 6 11.5 C6 11.5 2 7.5 2 4.5 A4 4 0 0 1 6 0.5 Z M6 3 A1.5 1.5 0 1 0 6 6 A1.5 1.5 0 1 0 6 3 Z" fill-rule="evenodd"/>
        </svg>
        <span>Coral Reach Shore, Grand Cayman, Cayman Islands</span>
      </li>
    </ul>
  </section>

  <section class="card card--back" aria-label="Card back">
    <div class="web-band">
      <svg class="web-icon" viewBox="0 0 20 20" aria-hidden="true" fill="none" stroke="#ffffff" stroke-width="1.6">
        <circle cx="10" cy="10" r="8.5" fill="#ffffff" stroke="none"/>
        <ellipse cx="10" cy="10" rx="3.5" ry="8.5" stroke="var(--band-blue)" stroke-width="1.2"/>
        <line x1="1.5" y1="10" x2="18.5" y2="10" stroke="var(--band-blue)" stroke-width="1.2"/>
        <line x1="3" y1="5.8" x2="17" y2="5.8" stroke="var(--band-blue)" stroke-width="1.2"/>
        <line x1="3" y1="14.2" x2="17" y2="14.2" stroke="var(--band-blue)" stroke-width="1.2"/>
      </svg>
      <span class="web-address">www.roamquill.net</span>
    </div>
  </section>
</main>
</body>
</html>
```